Lumenfield Holdings

Professional looking business card using darker colours
I do not yet have a logo for the company so feel free to suggest
The business is based on consultancy and project management
Based in Melbourne
Business card can omit the word "Holdings" and can be Lumenfield consulting etc.

Business

Contact Name on card : Tom Verisco Contact number : +61412 305 617 Email address will be confirmed shortly.

```html
<!DOCTYPE html>
<html lang="en">
<head>
<meta charset="utf-8">
<title>Lumenfield Consulting – Business Card</title>
<link rel="stylesheet" href="https://fonts.googleapis.com/css2?family=Alegreya+Sans:wght@400&family=Roboto+Condensed:wght@400;700&display=swap">
<style>
  :root {
    --backdrop: #1e1a19;
    --card-front: #f3f3f3;
    --card-back: #ffffff;
    --ink: #1f1b1a;
    --orange: #eca22e;
    --yellow: #f2d21e;
    --blue-deep: #0a80b8;
    --blue-light: #74c0e4;
  }
  html, body {
    margin: 0;
    padding: 0;
    width: 1058px;
    height: 1200px;
    overflow: hidden;
    background: var(--backdrop);
  }
  .canvas {
    position: relative;
    width: 1058px;
    height: 1200px;
    background: var(--backdrop);
  }
  .card {
    position: absolute;
    left: 151px;
    width: 757px;
    height: 433px;
    overflow: hidden;
  }
  .card--front {
    top: 124px;
    background: var(--card-front);
  }
  .card--back {
    top: 627px;
    background: var(--card-back);
  }
  .brand-art {
    position: absolute;
    left: 189px;
    top: 0;
    width: 166px;
    height: 433px;
    background: linear-gradient(180deg, rgba(116,192,228,0.35) 0%, rgba(236,162,46,0.35) 55%, rgba(242,210,30,0.3) 100%);
    border-radius: 80px 80px 80px 80px / 200px 200px 200px 200px;
  }
  .brand-name {
    position: absolute;
    left: 280px;
    top: 84px;
    width: 436px;
    margin: 0;
    text-align: center;
    font-family: "Alegreya Sans", sans-serif;
    font-weight: 400;
    font-size: 45px;
    line-height: 1;
    color: var(--ink);
    white-space: nowrap;
  }
  .contact {
    position: absolute;
    left: 280px;
    top: 175px;
    width: 436px;
    text-align: center;
    font-family: "Roboto Condensed", sans-serif;
    color: var(--ink);
  }
  .contact__name {
    margin: 0;
    font-weight: 700;
    font-size: 25px;
    line-height: 34px;
  }
  .contact__phone {
    margin: 0;
    font-weight: 400;
    font-size: 26px;
    line-height: 34px;
  }
  .band {
    position: absolute;
    left: 0;
    width: 757px;
    height: 44px;
  }
  .band--top {
    top: 0;
    background: linear-gradient(90deg, var(--orange), var(--yellow));
  }
  .band--bottom {
    bottom: 0;
    background: linear-gradient(90deg, var(--blue-deep), var(--blue-light));
  }
  .details {
    position: absolute;
    left: 74px;
    top: 88px;
    font-family: "Roboto Condensed", sans-serif;
    font-size: 23px;
    line-height: 31px;
    color: var(--ink);
  }
  .details p { margin: 0; }
  .tab {
    position: absolute;
    left: 0;
    top: 245px;
    width: 263px;
    height: 73px;
  }
</style>
</head>
<body>
<main class="canvas">
  <section class="card card--front">
    <div class="brand-art" role="img" aria-label="Flowing blue, orange and yellow brand ribbon"></div>
    <h1 class="brand-name">Lumenfield Consulting</h1>
    <div class="contact">
      <p class="contact__name">Tom Verisco</p>
      <p class="contact__phone">Contact Number : +61412 305 617</p>
    </div>
  </section>

  <section class="card card--back">
    <div class="band band--top"></div>
    <div class="details">
      <p>Email:</p>
      <p>Website:</p>
    </div>
    <svg class="tab" viewBox="0 0 263 73" aria-hidden="true">
      <path d="M0 0 H213 A50 50 0 0 1 263 50 V73 H0 Z" fill="var(--backdrop)"/>
    </svg>
    <div class="band band--bottom"></div>
  </section>
</main>
</body>
</html>
```